roofing door hanger

we would like to have our logo kvt roofing, it would be given when we are working in the neighborhood and have our services roof replacement, roof repair, ventilation, inspections. Our slogan is "Reliability starts at the top" . Our company is kvt roofing i would like to get one or two reviews from vorblin, and f any pictures are needed can use pellomart.

Industry/Entity Type

Roofing

Requirements
Must have
• this has to be a door hanger design

```html
<!DOCTYPE html>
<html lang="en">
<head>
<meta charset="utf-8">
<title>KVT Roofing Door Hanger</title>
<link rel="stylesheet" href="https://fonts.googleapis.com/css2?family=Titillium+Web:wght@600;700;900&display=swap">
<style>
  :root {
    --orange: #e08a1e;
    --brick: #9a4a24;
    --ink: #4d4d4d;
    --ink-dark: #3a3a3a;
    --paper: #f4f5f6;
    --white: #ffffff;
    --backdrop: #e4e1dc;
  }
  * { margin: 0; padding: 0; box-sizing: border-box; }
  html, body {
    width: 1120px; height: 1200px; overflow: hidden;
    background: var(--backdrop);
    font-family: "Titillium Web", "Arial Narrow", sans-serif;
  }
  .hanger {
    position: absolute; left: 210px; top: 10px;
    width: 700px; height: 1180px;
  }
  .hanger-art {
    position: absolute; inset: 0;
    filter: drop-shadow(0 6px 14px rgba(0,0,0,.18));
  }
  .top-phone {
    position: absolute; left: 36px; top: 196px;
    font-size: 46px; font-weight: 700; color: var(--ink);
    line-height: 1; letter-spacing: .5px;
  }
  .brand {
    position: absolute; right: 34px; top: 204px;
    display: flex; align-items: center; gap: 10px;
    color: var(--ink); font-weight: 700;
  }
  .brand-mark { width: 20px; height: 20px; background: var(--orange); }
  .brand-name { font-size: 34px; line-height: 1; letter-spacing: 1px; }
  .slogan {
    position: absolute; left: 40px; top: 560px;
    font-size: 58px; font-weight: 700; line-height: 64px;
    color: var(--white); text-transform: uppercase;
    text-shadow: 0 3px 6px rgba(0,0,0,.45);
  }
  .services { position: absolute; left: 40px; top: 812px; }
  .services-title {
    font-size: 32px; font-weight: 700; color: var(--ink-dark);
    line-height: 1; margin-bottom: 10px;
  }
  .services-list { list-style: none; }
  .services-list li {
    font-size: 24px; font-weight: 700; color: var(--orange);
    line-height: 30px; text-transform: uppercase;
    display: flex; align-items: center; gap: 10px;
  }
  .services-list li::before {
    content: ""; width: 8px; height: 8px; border-radius: 50%;
    background: var(--orange);
  }
  .reviews {
    position: absolute; left: 30px; right: 30px; top: 994px;
    display: flex; gap: 16px;
  }
  .review {
    flex: 1; background: var(--white);
    border-left: 5px solid var(--orange);
    padding: 8px 12px; height: 92px;
  }
  .review-stars { color: var(--orange); font-size: 16px; letter-spacing: 2px; line-height: 18px; }
  .review-text { font-size: 15px; font-weight: 600; color: var(--ink-dark); line-height: 19px; margin-top: 3px; }
  .review-author { font-size: 13px; font-weight: 700; color: var(--ink); margin-top: 3px; }
  .footer-rule {
    position: absolute; left: 0; right: 0; top: 1100px; height: 6px;
    background: var(--ink-dark);
  }
  .footer {
    position: absolute; left: 0; right: 0; top: 1106px; height: 74px;
    background: var(--orange);
    display: flex; align-items: center; justify-content: center;
    font-size: 32px; font-weight: 700; color: var(--white); letter-spacing: .5px;
  }
</style>
</head>
<body>
  <main class="hanger">
    <svg class="hanger-art" viewBox="0 0 700 1180" width="700" height="1180">
      <defs>
        <linearGradient id="heroTone" x1="0" y1="0" x2="1" y2="1">
          <stop offset="0" stop-color="#d9822a"/>
          <stop offset=".5" stop-color="#a8502a"/>
          <stop offset="1" stop-color="#6e3a26"/>
        </linearGradient>
        <linearGradient id="thumbGrey" x1="0" y1="0" x2="1" y2="1">
          <stop offset="0" stop-color="#a9adb1"/>
          <stop offset="1" stop-color="#55595e"/>
        </linearGradient>
      </defs>
      <path class="hanger-body" d="M0,40 Q0,0 40,0 H660 Q700,0 700,40 V1180 H0 Z" fill="var(--paper)"/>
      <circle class="hanger-hole" cx="350" cy="95" r="62" fill="var(--backdrop)"/>
      <line class="hanger-slit" x1="400" y1="125" x2="700" y2="172" stroke="var(--backdrop)" stroke-width="6"/>
      <polygon class="hero-photo" role="img" aria-label="Photo of two roofers working on a shingled roof of a brick house with a chimney"
        points="0,462 220,320 700,470 700,790 0,790" fill="url(#heroTone)"/>
      <polyline class="roof-band" points="-10,440 220,290 710,450" fill="none" stroke="var(--orange)" stroke-width="13"/>
      <g class="thumbs" stroke="var(--white)" stroke-width="5">
        <rect role="img" aria-label="Photo of a hammer fixing roof shingles" x="500" y="420" width="170" height="130" fill="url(#thumbGrey)"/>
        <rect role="img" aria-label="Photo of a worker torch-sealing a flat roof membrane" x="500" y="562" width="170" height="130" fill="url(#thumbGrey)"/>
        <rect role="img" aria-label="Photo of hands placing roof panels on wooden battens" x="500" y="704" width="170" height="130" fill="url(#thumbGrey)"/>
        <rect role="img" aria-label="Photo of gloved hands laying grey roof tiles" x="500" y="846" width="170" height="130" fill="url(#thumbGrey)"/>
      </g>
    </svg>

    <div class="top-phone">555-014-2290</div>

    <div class="brand">
      <span class="brand-mark"></span>
      <span class="brand-name">KVT ROOFING</span>
    </div>

    <h1 class="slogan">Reliability<br>starts at<br>the top</h1>

    <section class="services">
      <h2 class="services-title">OUR SERVICES:</h2>
      <ul class="services-list">
        <li>Roof Replacement</li>
        <li>Roof Repair</li>
        <li>Ventilation</li>
        <li>Inspections</li>
      </ul>
    </section>

    <section class="reviews">
      <article class="review">
        <div class="review-stars">★★★★★</div>
        <p class="review-text">“Fast, clean roof replacement. The crew was on time every day.”</p>
        <p class="review-author">— Dana M., Vorblin review</p>
      </article>
      <article class="review">
        <div class="review-stars">★★★★★</div>
        <p class="review-text">“Honest inspection and a fair quote. Highly recommend KVT.”</p>
        <p class="review-author">— Luis R., Vorblin review</p>
      </article>
    </section>

    <div class="footer-rule"></div>
    <footer class="footer">KVT-ROOFING.COM | 555-014-2290</footer>
  </main>
</body>
</html>
```